Construction company stationary design

We're wanting to develop a new professional stationary set for a newly establised property related business using our existing logo (attached). Business incorporates renovations, property investment and property development.

Specifically needing letter head, business cards, envelopes, email signature and need to get tshirt and caps embroydered.

Looking for something quite modern but professional using white, black and green.

```html
<!DOCTYPE html>
<html lang="en">
<head>
<meta charset="utf-8">
<title>Halvard Build — Business Card</title>
<link rel="stylesheet" href="https://fonts.googleapis.com/css2?family=Barlow:wght@400;500;700&display=swap">
<style>
  :root {
    --green: #8cc63f;
    --white: #ffffff;
    --ink: #1a1a1a;
    --grey-text: #6d6d6d;
    --stage: #d9d9d9;
    --card-shadow: rgba(0, 0, 0, 0.18);
  }
  * { box-sizing: border-box; margin: 0; padding: 0; }
  html, body {
    width: 1200px; height: 800px; overflow: hidden;
    background: var(--stage);
    font-family: "Barlow", Arial, sans-serif;
  }
  .card-set {
    position: absolute; inset: 0;
    display: flex; align-items: center; justify-content: center; gap: 48px;
  }
  .card {
    position: relative;
    width: 540px; height: 310px;
    border-radius: 28px;
    box-shadow: 0 10px 26px var(--card-shadow);
    overflow: hidden;
  }

  /* Front */
  .card-front { background: var(--white); }
  .contact-name {
    position: absolute; left: 40px; top: 56px;
    color: var(--green); font-size: 27px; font-weight: 400; letter-spacing: 0.5px;
  }
  .contact-title {
    position: absolute; left: 40px; top: 88px;
    color: var(--ink); font-size: 13px; font-weight: 500;
  }
  .contact-rows { position: absolute; left: 40px; top: 114px; }
  .contact-row {
    display: flex; align-items: center; gap: 7px;
    color: var(--grey-text); font-size: 16px; letter-spacing: 0.4px; height: 24px;
    white-space: nowrap;
  }
  .label-box {
    display: inline-flex; align-items: center; justify-content: center;
    width: 17px; height: 17px; background: var(--green);
    color: var(--white); font-size: 13px; font-weight: 500;
  }
  .divider {
    position: absolute; left: 40px; top: 172px; width: 300px; height: 2px;
    background: var(--ink);
  }
  .address {
    position: absolute; left: 40px; top: 180px;
    color: var(--grey-text); font-size: 15.5px; line-height: 20px; letter-spacing: 0.4px;
  }
  .phone-pair {
    position: absolute; left: 40px; top: 224px;
    display: flex; gap: 14px;
  }
  .social-links {
    position: absolute; right: 40px; top: 60px; display: flex; gap: 5px;
  }
  .social-links span {
    width: 16px; height: 16px; border-radius: 3px; background: var(--green);
  }
  .brand {
    font-family: "Barlow", Arial, sans-serif; font-weight: 700;
    display: flex; align-items: center; gap: 10px; letter-spacing: 0.5px;
  }
  .brand-mark { width: 22px; height: 22px; flex: none; }
  .brand-name { line-height: 1; }
  .card-front .brand {
    position: absolute; right: 40px; bottom: 36px;
    color: var(--green); font-size: 32px;
  }
  .card-front .brand-mark { background: var(--green); }

  /* Back */
  .card-back { background: var(--green); }
  .web-address {
    position: absolute; left: 44px; top: 30px;
    color: var(--white); font-size: 13px; letter-spacing: 1px;
  }
  .card-back .brand {
    position: absolute; left: 44px; top: 118px;
    color: var(--white); font-size: 38px;
  }
  .card-back .brand-mark { background: var(--white); }
</style>
</head>
<body>
<main class="card-set">
  <section class="card card-front" aria-label="Business card front">
    <h1 class="contact-name">Marcus Avery</h1>
    <p class="contact-title">Managing Director</p>
    <div class="contact-rows">
      <p class="contact-row"><span class="label-box">M</span>123-456-7890</p>
      <p class="contact-row"><span class="label-box">E</span>marcus@halvardbuild.com</p>
    </div>
    <div class="divider"></div>
    <p class="address">Office #, Building #, Street<br>City, Country XXXXX</p>
    <div class="phone-pair">
      <p class="contact-row"><span class="label-box">P</span>123-456-7890</p>
      <p class="contact-row"><span class="label-box">F</span>123-456-7890</p>
    </div>
    <div class="social-links" aria-label="Social profiles">
      <span></span><span></span><span></span><span></span>
    </div>
    <div class="brand"><span class="brand-mark"></span><span class="brand-name">Halvard<br>Build</span></div>
  </section>

  <section class="card card-back" aria-label="Business card back">
    <p class="web-address">halvardbuild.com</p>
    <div class="brand"><span class="brand-mark"></span><span class="brand-name">Halvard<br>Build</span></div>
  </section>
</main>
</body>
</html>
```